Thornbeck Advisory Group Business Card Design Project

2-sided business card for my small (me and a couple subcontractors) firm, which consults to public community colleges and school districts and public agencies in California on energy matters, mostly solar electric systems that can reduce their electricity use by as much as 80%. I prepare requests for proposals (RFPs), manage the RFP processes, and work with the solar vendors to get the best deal for my clients. I also do regulatory and legislative advocacy for strong renewable energy policies. I do lots of quantitative analysis to make sure the solar systems are sized to produce the maximum monetary savings and focus a lot on the aesthetic design of the solar systems, as architectural features of the campuses (most are carport structures built in parking lots, but some are built on the ground and on rooftops). All my work is geared to getting the best value, highest quality, and most reliable solar system. My career background is in public interest energy advocacy; I'm not a consultant trying to make a million dollars but someone who is still serving in the public interest.

My competition is made up of much larger firms; this business card/logo in large part is intended to present an image of my firm as an equal to these larger firms despite my smaller size.

Essential information as follows:
Firm name: Thornbeck Advisory Group
Tagline: Clean Energy Procurement for the Public Sector
Name: Walter Pennick
email, 2 phone number, and address listed as well.

Target Market(s)

Public schools, community colleges, & public agencies.There is a wide range in the sophistication of these organizations.

Industry/Entity Type

Parking

Requirements
Must have
• - several rich colors, which can be either in the logo or in the background - the overall feeling of the card should reflect richness of color. I have uploaded some photos showing some colors that I like together. By rich I do not necessarily mean bright. I suppose bright colors in the logo could be supported with rich colors in the overall background of the card.
- professional, and powerful in an understated way (not kooky, cartoonish, or very playful)
- the logo must NOT be too representational of solar energy or the sun, but at the same time it would be good for the logo to be somewhat suggestive of this.

Nice to have
• -I like abstract and geometric images (with rich colts).
- A very subtle reference to schools/colleges/education would be great but it CANNOT be explicit; it would have to be faintly suggestive.
- In the logo I like the idea of abstract or geometric shapes intersecting with other in an interesting and suggestive way, conveying the multiple aspects of my practice (economics, data analysis, energy analysis, problem solving, managing collaborative processes, policy analysis)
- My work relates to environmental concerns, especially climate change. Working this into the logo in a subtle way could be good, but it's not a requirement.
- I like the idea that the logo/card feels serene.
- In designing the business card, I kind of like the idea of having the tag line as the first thing they read, then they see the firm name.

Should not have
• Not:
- humorous
- boring
- overly slick
- overly formal
- whimsical

```html
<!DOCTYPE html>
<html lang="en">
<head>
<meta charset="utf-8">
<title>Thornbeck Advisory Group — Business Card</title>
<link rel="stylesheet" href="https://fonts.googleapis.com/css2?family=Didact+Gothic&family=Mulish:wght@700&display=swap">
<style>
  :root {
    --page: #e4e1e2;
    --card-white: #f7f6f4;
    --ink: #3a3a3c;
    --ink-soft: #55555a;
    --plum: #4a0a26;
    --plum-deep: #3c061d;
    --on-plum: #ece3e7;
    --accent: #e38a1e;
  }
  * { margin: 0; padding: 0; box-sizing: border-box; }
  html, body { width: 1200px; height: 800px; overflow: hidden; }
  body {
    background: var(--page);
    font-family: "Didact Gothic", "Century Gothic", sans-serif;
    color: var(--ink);
    display: flex;
    align-items: center;
    justify-content: center;
    gap: 40px;
  }
  .card {
    position: relative;
    width: 525px;
    height: 300px;
    box-shadow: 0 10px 30px rgba(40, 10, 25, 0.18);
  }
  .card--front { background: var(--card-white); }
  .card--back { background: linear-gradient(160deg, var(--plum) 0%, var(--plum-deep) 100%); color: var(--on-plum); }

  .wordmark {
    display: flex;
    align-items: center;
    gap: 10px;
    font-family: "Didact Gothic", "Century Gothic", sans-serif;
    font-weight: 400;
    letter-spacing: 0.01em;
    white-space: nowrap;
  }
  .wordmark__square { width: 14px; height: 14px; background: var(--accent); flex: none; }

  .card--front .wordmark { position: absolute; left: 34px; top: 78px; font-size: 23px; color: var(--ink); }

  .tagline { font-size: 13.5px; line-height: 1.2; }
  .card--front .tagline { position: absolute; left: 318px; top: 40px; color: var(--ink-soft); }

  .person { position: absolute; left: 318px; top: 150px; }
  .person__name { font-family: "Mulish", "Century Gothic", sans-serif; font-weight: 700; font-size: 14.5px; letter-spacing: 0.03em; color: var(--ink); }
  .person__title { font-size: 12.5px; color: var(--ink-soft); margin-top: 2px; }

  .phones { position: absolute; left: 318px; top: 210px; font-size: 12.5px; line-height: 1.3; color: var(--ink-soft); }
  .phones b { font-family: "Mulish", "Century Gothic", sans-serif; font-weight: 700; color: var(--ink); }

  .contact { position: absolute; left: 34px; bottom: 30px; font-size: 13px; line-height: 1.3; color: var(--ink-soft); }

  .card--back .tagline { position: absolute; left: 40px; top: 46px; font-size: 16px; color: var(--on-plum); }
  .card--back .wordmark { position: absolute; left: 40px; bottom: 56px; font-size: 28px; color: var(--on-plum); }
</style>
</head>
<body>
  <section class="card card--front" aria-label="Card front">
    <p class="tagline">Procuring Clean Energy<br>for the Public Sector</p>
    <div class="wordmark"><span>Thornbeck Advisory Group</span><span class="wordmark__square"></span></div>
    <div class="person">
      <p class="person__name">WALTER PENNICK</p>
      <p class="person__title">Principal</p>
    </div>
    <p class="phones"><b>office:</b> (555) 014-2281<br><b>mobile:</b> (555) 014-7390</p>
    <p class="contact">walter@thornbeckadvisory.com<br>2250 Larkfield Ave., Brierton, CA 94011</p>
  </section>

  <section class="card card--back" aria-label="Card back">
    <p class="tagline">Procuring Clean Energy<br>for the Public Sector</p>
    <div class="wordmark"><span>Thornbeck Advisory Group</span><span class="wordmark__square"></span></div>
  </section>
</body>
</html>
```